The Restful Airway & Jaw Clinic of Larchmont
Corinne T. Valdez D.D.S., Pharm.D, LVIF
The Restful Airway & Jaw Clinic of Larchmont - Health
Creative Brief
Use specific fonts
Use what works the best in your design
Professional
The Restful Airway & Jaw Clinic of LM
37 Gorse Lane Fenwick, OR 97431
cvaldezdds@quillmail.net
I like colors in Greens and complimentary colors. I prefers logos that are more abstract in design with elegant (not cursive) fonts. I am drawn to logos which look like abstract "faces" or "symbols". I treat many patients who are in pain, and would like my logo and design to exude a sense of well-being and serenity. I would like the logo to focus more on the "sleep" aspect (perhaps an abstract of a person sleeping?). Please no teeth or dental symbols! Please use several complimentary colors in the design. You may abbreviate "Larchmont" to "LM" if it works better in your design

```html
<!DOCTYPE html>
<html lang="en">
<head>
<meta charset="utf-8">
<title>The Restful Airway &amp; Jaw Clinic of Larchmont – Stationery</title>
<link rel="stylesheet" href="https://fonts.googleapis.com/css2?family=Lato:wght@400;700&display=swap">
<style>
:root{
  --olive:#9c976a;
  --olive-dark:#6e6a43;
  --olive-light:#d9d6bd;
  --cream:#efeee2;
  --ink:#4e4a2c;
  --paper:#ffffff;
  --window-line:#c9c7b6;
  --backdrop:#ffffff;
}
*{box-sizing:border-box;margin:0;padding:0}
html,body{width:1200px;height:785px;overflow:hidden;background:var(--backdrop)}
body{position:relative;font-family:"Lato",Arial,sans-serif;color:var(--ink)}
.piece{position:absolute;overflow:hidden;box-shadow:0 2px 6px rgba(0,0,0,.18)}
.piece svg.bg{position:absolute;inset:0;width:100%;height:100%}

/* envelopes */
.envelope{width:600px;height:336px;background:var(--paper)}
.envelope--top{left:12px;top:48px}
.envelope--bottom{left:12px;top:437px}
.brand{position:absolute;display:flex;align-items:center;gap:10px}
.brand__dot{width:34px;height:34px;border-radius:50%;background:var(--olive);flex:none}
.brand__name{font-weight:400;color:var(--olive-dark);line-height:1.05}
.brand__name .line1{display:block;font-size:22px}
.brand__name .line2{display:block;font-size:11px;letter-spacing:.5px;text-transform:uppercase}
.envelope .brand{left:28px;top:58px}
.address{position:absolute;font-size:10.5px;line-height:1.45;color:var(--ink)}
.envelope .address{left:30px;top:172px}
.window{position:absolute;left:345px;top:192px;width:180px;height:92px;border:1.5px solid var(--window-line);border-radius:6px;background:rgba(255,255,255,.85)}

/* letterhead */
.letterhead{left:630px;top:10px;width:560px;height:768px;background:var(--paper)}
.letterhead .brand{left:0;right:0;top:10px;flex-direction:column;gap:8px;text-align:center}
.letterhead .brand__dot{width:40px;height:40px}
.letterhead .brand__name .line1{font-size:26px}
.letterhead .address{right:24px;bottom:30px;text-align:right}

/* business cards */
.card{width:282px;height:104px;border-radius:8px;left:667px}
.card--front{top:557px}
.card--back{top:672px}
.card .brand{left:18px;top:28px}
.card .brand__dot{width:26px;height:26px}
.card .brand__name .line1{font-size:16px}
.card .brand__name .line2{font-size:8px}
.card-back__logo{position:absolute;left:0;right:0;top:8px;display:flex;justify-content:center;align-items:center;gap:6px;font-size:11px;color:var(--olive-dark)}
.card-back__logo span.dot{width:14px;height:14px;border-radius:50%;background:#7d2f2c}
.card-back__person{position:absolute;right:14px;top:42px;text-align:right;font-size:8px;line-height:1.35}
.card-back__person strong{font-size:10px;display:block}
.card .address{left:14px;top:60px;font-size:7px;line-height:1.35}
</style>
</head>
<body>

<!-- envelope: flap open -->
<section class="piece envelope envelope--top">
  <svg class="bg" viewBox="0 0 600 336" aria-hidden="true">
    <defs>
      <linearGradient id="envFill" x1="0" y1="0" x2="1" y2="1">
        <stop offset="0" stop-color="#f4f3ea"/><stop offset="1" stop-color="#e2e0ca"/>
      </linearGradient>
      <linearGradient id="flapFill" x1="0" y1="0" x2="0" y2="1">
        <stop offset="0" stop-color="#8d8859"/><stop offset="1" stop-color="#b6b28a"/>
      </linearGradient>
    </defs>
    <rect width="600" height="336" fill="url(#envFill)"/>
    <path d="M0 336 C120 250 330 150 600 170 L600 336 Z" fill="#fff" opacity=".75"/>
    <path d="M0 0 H600 L300 78 Z" fill="url(#flapFill)"/>
    <circle cx="300" cy="60" r="20" fill="var(--olive-dark)" stroke="#fff" stroke-width="2"/>
  </svg>
  <div class="brand">
    <span class="brand__dot"></span>
    <span class="brand__name"><span class="line1">The Restful Airway</span><span class="line2">&amp; Jaw Clinic of Larchmont</span></span>
  </div>
  <p class="address">37 Gorse Lane<br>Fenwick, OR 97431<br>Phone: 541-555-0142<br>Fax: 541-555-0187<br>Email: cvaldezdds@quillmail.net</p>
  <div class="window"></div>
</section>

<!-- envelope: flap closed -->
<section class="piece envelope envelope--bottom">
  <svg class="bg" viewBox="0 0 600 336" aria-hidden="true">
    <defs>
      <linearGradient id="envFill2" x1="0" y1="0" x2="1" y2="1">
        <stop offset="0" stop-color="#e6e4d0"/><stop offset="1" stop-color="#c9c5a3"/>
      </linearGradient>
    </defs>
    <rect width="600" height="336" fill="url(#envFill2)"/>
    <path d="M0 0 H600 L300 70 Z" fill="#fff" opacity=".55"/>
    <path d="M0 336 C150 260 360 200 600 230 L600 336 Z" fill="#fff" opacity=".35"/>
    <circle cx="300" cy="28" r="20" fill="var(--olive-dark)" stroke="#fff" stroke-width="2"/>
  </svg>
  <div class="brand" style="top:100px">
    <span class="brand__dot"></span>
    <span class="brand__name"><span class="line1">The Restful Airway</span><span class="line2">&amp; Jaw Clinic of Larchmont</span></span>
  </div>
  <p class="address" style="top:205px">37 Gorse Lane<br>Fenwick, OR 97431<br>Phone: 541-555-0142<br>Fax: 541-555-0187<br>Email: cvaldezdds@quillmail.net</p>
</section>

<!-- letterhead -->
<section class="piece letterhead">
  <svg class="bg" viewBox="0 0 560 768" aria-hidden="true">
    <defs>
      <linearGradient id="sweep" x1="0" y1="0" x2="1" y2="0">
        <stop offset="0" stop-color="#fff"/><stop offset="1" stop-color="#cfcbac"/>
      </linearGradient>
    </defs>
    <path d="M120 768 C220 640 420 560 560 560 L560 768 Z" fill="url(#sweep)"/>
    <path d="M200 768 C290 680 440 630 560 625 L560 768 Z" fill="#fff" opacity=".85"/>
  </svg>
  <div class="brand">
    <span class="brand__dot"></span>
    <span class="brand__name"><span class="line1">The Restful Airway</span><span class="line2">&amp; Jaw Clinic of Larchmont</span></span>
  </div>
  <p class="address">37 Gorse Lane<br>Fenwick, OR 97431<br>Phone: 541-555-0142<br>Fax: 541-555-0187<br>Email: cvaldezdds@quillmail.net</p>
</section>

<!-- business card front -->
<section class="piece card card--front">
  <svg class="bg" viewBox="0 0 282 104" preserveAspectRatio="none" aria-hidden="true">
    <defs>
      <linearGradient id="cardFill" x1="0" y1="0" x2="1" y2="1">
        <stop offset="0" stop-color="#eae8d6"/><stop offset="1" stop-color="#b3af87"/>
      </linearGradient>
    </defs>
    <rect width="282" height="104" fill="url(#cardFill)"/>
    <path d="M0 104 C80 70 190 60 282 70 L282 104 Z" fill="#fff" opacity=".35"/>
  </svg>
  <div class="brand">
    <span class="brand__dot" style="background:#7d2f2c"></span>
    <span class="brand__name"><span class="line1">The Restful Airway</span><span class="line2">&amp; Jaw Clinic of Larchmont</span></span>
  </div>
</section>

<!-- business card back -->
<section class="piece card card--back">
  <svg class="bg" viewBox="0 0 282 104" preserveAspectRatio="none" aria-hidden="true">
    <rect width="282" height="104" fill="url(#cardFill)"/>
    <path d="M0 104 C80 80 190 70 282 78 L282 104 Z" fill="#fff" opacity=".35"/>
  </svg>
  <div class="card-back__logo"><span class="dot"></span>The Restful Airway &amp; Jaw Clinic of LM</div>
  <p class="card-back__person"><strong>Corinne T. Valdez</strong>D.D.S., Pharm.D, LVIF<br>Phone: 541-555-0142<br>Fax: 541-555-0187<br>Email: cvaldezdds@quillmail.net</p>
  <p class="address">37 Gorse Lane<br>Fenwick, OR 97431</p>
</section>

</body>
</html>
```